Business card for our large format printing and installation business

We want a professional looking business card for our business. We manufacture and install Signs.

On the back of the card add this info
Large Format Graphics Printing & Installations, Event Graphics, Banners, Posters, Vehicle Fleet Graphics, Boat Wraps, Wall Murals, Decals,Displays,Signs,Plaques,Digital Signs

On the Front of the card add the Tallowfern Signs logo, plus On the back of the card add the Orange Tallowfern Wraps logo. The 2 vector logos are attached to the design brief.

Target Market(s)

Local business owners

Contact Information for Business Card

Colors
f37122
f68d4e
f9ba93

Requirements
Must have
• On the Front of the card add the Tallowfern Signs logo, plus On the back of the card add the Orange Tallowfern Wraps logo. The 2 vector logos are attached to the design brief.

```html
<!DOCTYPE html>
<html lang="en">
<head>
<meta charset="utf-8">
<title>Tallowfern Signs – Business Card</title>
<link href="https://fonts.googleapis.com/css2?family=Lato:wght@400;700;900&display=swap" rel="stylesheet">
<style>
  :root{
    --stage:#dcdcdc;
    --card:#1f1d1d;
    --gold:#f6b417;
    --gold-light:#fde04a;
    --orange:#f37122;
    --orange-mid:#f68d4e;
    --text:#f1f1f1;
    --muted:#c9c9c9;
  }
  *{box-sizing:border-box;margin:0;padding:0}
  html,body{width:1200px;height:787px;overflow:hidden;background:var(--stage);font-family:"Lato",sans-serif}
  .sheet{width:1200px;height:787px;display:flex;align-items:center;justify-content:center;gap:36px}
  .card{position:relative;width:560px;height:320px;background:var(--card);box-shadow:0 6px 18px rgba(0,0,0,.25);overflow:hidden}
  .card__band{position:absolute;left:0;right:0;bottom:12px;height:16px;
    background:linear-gradient(90deg,var(--gold) 0%,var(--gold-light) 22%,var(--orange) 48%,var(--gold) 70%,var(--gold-light) 88%,var(--orange-mid) 100%)}
  .wordmark{font-weight:900;color:var(--gold);line-height:1;letter-spacing:.5px}

  /* front */
  .front__person{position:absolute;left:34px;top:34px}
  .front__name{font-weight:700;font-size:19px;color:var(--gold);text-transform:uppercase;letter-spacing:.3px}
  .front__title{font-size:13px;color:var(--muted);margin-top:3px}
  .front__logo{position:absolute;right:34px;top:42px;text-align:right;font-size:38px}
  .front__rule{position:absolute;left:34px;right:34px;top:132px;height:1.5px;
    background:linear-gradient(90deg,var(--gold),var(--orange))}
  .contact{position:absolute;left:34px;top:152px;list-style:none}
  .contact li{display:flex;align-items:center;gap:10px;font-size:14px;color:var(--text);height:23px}
  .contact svg{width:13px;height:13px;fill:var(--gold)}
  .front__address{position:absolute;right:34px;top:170px;text-align:right;font-size:14px;color:var(--text);line-height:1.55}

  /* back */
  .back__logo{position:absolute;left:0;right:0;top:62px;text-align:center;font-size:42px}
  .back__services{position:absolute;left:20px;right:20px;top:142px;text-align:center;font-size:13.5px;color:var(--text);line-height:1.65}
</style>
</head>
<body>
<main class="sheet">

  <section class="card card--front" aria-label="Business card front">
    <div class="front__person">
      <p class="front__name">Dorian Vasquez</p>
      <p class="front__title">Owner</p>
    </div>
    <p class="front__logo wordmark">Tallowfern Signs</p>
    <div class="front__rule"></div>
    <ul class="contact">
      <li><svg viewBox="0 0 24 24" aria-hidden="true"><path d="M6.6 10.8a15.1 15.1 0 0 0 6.6 6.6l2.2-2.2a1 1 0 0 1 1-.25 11.4 11.4 0 0 0 3.6.6 1 1 0 0 1 1 1V20a1 1 0 0 1-1 1A17 17 0 0 1 3 4a1 1 0 0 1 1-1h3.5a1 1 0 0 1 1 1c0 1.25.2 2.45.6 3.6a1 1 0 0 1-.25 1z"/></svg>410.555.0187</li>
      <li><svg viewBox="0 0 24 24" aria-hidden="true"><path d="M6 2h12v6H6zM4 9h16a2 2 0 0 1 2 2v6h-4v5H6v-5H2v-6a2 2 0 0 1 2-2zm4 8v3h8v-3z"/></svg>410.555.0188</li>
      <li><svg viewBox="0 0 24 24" aria-hidden="true"><path d="M2 5h20v14H2zm2 2v.5l8 5 8-5V7z"/></svg>hello@tallowfernsigns.com</li>
      <li><svg viewBox="0 0 24 24" aria-hidden="true"><path d="M12 2a10 10 0 1 0 0 20 10 10 0 0 0 0-20zm6.9 6h-2.9a15 15 0 0 0-1.4-3.6A8 8 0 0 1 18.9 8zM12 4a13 13 0 0 1 1.9 4h-3.8A13 13 0 0 1 12 4zM4.3 14a8 8 0 0 1 0-4h3.4a16 16 0 0 0 0 4zm.8 2h2.9a15 15 0 0 0 1.4 3.6A8 8 0 0 1 5.1 16zM8 8H5.1a8 8 0 0 1 4.3-3.6A15 15 0 0 0 8 8zm4 12a13 13 0 0 1-1.9-4h3.8A13 13 0 0 1 12 20zm2.3-6H9.7a14 14 0 0 1 0-4h4.6a14 14 0 0 1 0 4zm.3 5.6A15 15 0 0 0 16 16h2.9a8 8 0 0 1-4.3 3.6zM16.3 14a16 16 0 0 0 0-4h3.4a8 8 0 0 1 0 4z"/></svg>www.tallowfernsigns.com</li>
    </ul>
    <address class="front__address" style="font-style:normal">2280 Marrowgate Rd<br>Suite 14<br>Hollins Ferry, MD 21390</address>
    <div class="card__band"></div>
  </section>

  <section class="card card--back" aria-label="Business card back">
    <p class="back__logo wordmark">Tallowfern Wraps</p>
    <p class="back__services">Large Format Graphics Printing &amp; Installations, Event Graphics, Banners, Posters<br>Vehicle Fleet Graphics, Boat Wraps, Wall Murals, Decals<br>Displays, Signs, Plaques, Digital Signs</p>
    <div class="card__band"></div>
  </section>

</main>
</body>
</html>
```